Dr. Marissa Tevlin Medical/Chiropractic Business Card

Dr. Tevlin is a chiropractor and will require a business card that she uses every single day to book appointments on the back side of the card. Currently the office name goes by Dr. Marissa Tevlin. The chiropractic profession is based on the diagnosis and manipulative treatment of misalignments of the joints, especially those of the spinal column, which are held to cause other disorders by affecting the nerves, muscles, and organs. Dr. Marissa Tevlin is looking for a contemporary and minimalistic design.

Industry/Entity Type

Medical

Contact Information for Business Card

Name: Dr. Marissa Tevlin; Address: 748 Harcastle Rd South, London, ON N5R 2K7; Phone Number: 519.274.6193; Fax: 519.281.5046; email: marissa.tevlin@quorvamail.com

Requirements
Must have
• ability to write multiple appointments date/time on the back of card

```html
<!DOCTYPE html>
<html lang="en">
<head>
<meta charset="utf-8">
<title>Dr. Marissa Tevlin — Appointment Card</title>
<link rel="stylesheet" href="https://fonts.googleapis.com/css2?family=Lato:ital,wght@0,300;0,400;0,700;1,300;1,400&display=swap">
<style>
  :root {
    --page-bg: #eeeeec;
    --card-bg: #ffffff;
    --ink: #3a3a3a;
    --ink-soft: #555555;
    --green: #5dbb46;
    --green-light: #92d46f;
    --green-dark: #3fa83a;
    --cell-grey: #d8d8d5;
  }
  * { box-sizing: border-box; margin: 0; padding: 0; }
  html, body { width: 1200px; height: 1200px; overflow: hidden; }
  body {
    background: var(--page-bg);
    font-family: "Lato", sans-serif;
    color: var(--ink);
    display: flex; align-items: center; justify-content: center;
  }
  .card {
    position: relative;
    width: 600px; height: 1050px;
    background: var(--card-bg);
    box-shadow: 0 10px 30px rgba(0,0,0,0.12);
    padding: 80px 55px 0 55px;
  }
  .card-title {
    font-weight: 400; font-size: 56px; letter-spacing: 1px;
    color: var(--ink); line-height: 1;
  }
  .title-rule { height: 3px; background: var(--green); margin-top: 16px; width: 100%; }
  .column-heads {
    display: flex; margin-top: 22px; height: 34px; align-items: center;
    font-size: 17px; letter-spacing: 1px; text-transform: uppercase; color: var(--ink-soft);
  }
  .column-head { display: flex; align-items: center; gap: 10px; }
  .column-head.date { width: 300px; padding-left: 10px; }
  .column-head.time { padding-left: 10px; }
  .column-head svg { width: 26px; height: 26px; }
  .slots { margin-top: 20px; display: flex; flex-direction: column; gap: 6px; }
  .slot { display: flex; height: 50px; }
  .slot-accent { width: 6px; background: var(--green); margin-right: 6px; }
  .slot-date { width: 283px; background: var(--cell-grey); }
  .slot-time { flex: 1; background: linear-gradient(90deg, var(--green-light), var(--green)); }
  .booking-note {
    margin-top: 46px; margin-left: 40px;
    border-left: 5px solid var(--green);
    padding: 6px 0 6px 44px;
    font-style: italic; font-weight: 300; font-size: 27px; line-height: 1.3;
  }
  .booking-note .phone { color: var(--green); font-style: normal; font-weight: 400; }
  .info-head {
    margin-top: 38px; display: flex; align-items: flex-end; gap: 14px;
  }
  .info-head svg { width: 34px; height: 38px; flex: none; }
  .info-label-wrap { flex: 1; }
  .info-label { color: var(--green); font-size: 21px; font-weight: 400; padding-left: 4px; }
  .info-rule { height: 3px; background: var(--green); margin-top: 6px; }
  .info-text {
    margin-top: 16px; font-size: 16px; line-height: 1.45; color: var(--ink);
  }
</style>
</head>
<body>
  <main class="card">
    <h1 class="card-title">APPOINTMENTS</h1>
    <div class="title-rule"></div>

    <div class="column-heads">
      <div class="column-head date">
        <svg viewBox="0 0 26 26" aria-hidden="true">
          <circle cx="13" cy="13" r="11" fill="none" stroke="#5dbb46" stroke-width="2"/>
          <line x1="8" y1="10" x2="18" y2="10" stroke="#5dbb46" stroke-width="2"/>
          <line x1="8" y1="13.5" x2="18" y2="13.5" stroke="#5dbb46" stroke-width="2"/>
          <line x1="8" y1="17" x2="18" y2="17" stroke="#5dbb46" stroke-width="2"/>
        </svg>
        <span>Date</span>
      </div>
      <div class="column-head time">
        <svg viewBox="0 0 26 26" aria-hidden="true">
          <path d="M23 13a10 10 0 1 1-3-7.1" fill="none" stroke="#5dbb46" stroke-width="2"/>
          <polyline points="20,2 20,6.5 15.5,6.5" fill="none" stroke="#5dbb46" stroke-width="2"/>
          <polyline points="13,8 13,14 9,16" fill="none" stroke="#5dbb46" stroke-width="2"/>
        </svg>
        <span>Time:</span>
      </div>
    </div>

    <div class="slots">
      <div class="slot"><div class="slot-accent"></div><div class="slot-date"></div><div class="slot-time"></div></div>
      <div class="slot"><div class="slot-accent"></div><div class="slot-date"></div><div class="slot-time"></div></div>
      <div class="slot"><div class="slot-accent"></div><div class="slot-date"></div><div class="slot-time"></div></div>
      <div class="slot"><div class="slot-accent"></div><div class="slot-date"></div><div class="slot-time"></div></div>
      <div class="slot"><div class="slot-accent"></div><div class="slot-date"></div><div class="slot-time"></div></div>
      <div class="slot"><div class="slot-accent"></div><div class="slot-date"></div><div class="slot-time"></div></div>
      <div class="slot"><div class="slot-accent"></div><div class="slot-date"></div><div class="slot-time"></div></div>
      <div class="slot"><div class="slot-accent"></div><div class="slot-date"></div><div class="slot-time"></div></div>
    </div>

    <p class="booking-note">To schedule an appointment, please call us at <span class="phone">519.274.6193</span> during our normal business hours.</p>

    <div class="info-head">
      <svg viewBox="0 0 34 38" aria-hidden="true">
        <path d="M3 3h28v24l-8 8H3z" fill="none" stroke="#333" stroke-width="2.5"/>
        <path d="M23 35v-8h8" fill="none" stroke="#333" stroke-width="2.5"/>
        <line x1="9" y1="11" x2="25" y2="11" stroke="#333" stroke-width="2.5"/>
        <line x1="9" y1="17" x2="25" y2="17" stroke="#333" stroke-width="2.5"/>
        <line x1="9" y1="23" x2="19" y2="23" stroke="#333" stroke-width="2.5"/>
      </svg>
      <div class="info-label-wrap">
        <div class="info-label">Information:</div>
        <div class="info-rule"></div>
      </div>
    </div>
    <p class="info-text">If you are unable to keep your appointment, please notify the office at least 24 hours before the appointment time to re-schedule and to allow other patients to use the time.</p>
  </main>
</body>
</html>
```